Business Cards and Stationery for software company
For Software Company
Use same font as used in my logo
Eurostile-Black, Eurostile Extended #2
Bright & Fun-filled
Dorian Welby
Vice President
40627 NE 73rd Avenue Suite 815
Harlow Bay, WA 98731
dorianw@tandrafix.com
www.tandrafix.com
Please keep it simple. I'm open to other fonts as long as they work with the Eurostile we currently use. Arial will be the basis for our website. Don't need to include address necessarily

```html
<!DOCTYPE html>
<html lang="en">
<head>
<meta charset="utf-8">
<title>Tandrafix Stationery</title>
<link href="https://fonts.googleapis.com/css2?family=Michroma&family=Arimo:wght@400;700&display=swap" rel="stylesheet">
<style>
:root{
  --bg:#e9e9ea;
  --paper:#ffffff;
  --band:#3d3d3f;
  --accent:#d8262e;
  --ink:#4a4a4c;
  --muted:#8a8a8c;
  --faint:#f3d3d4;
}
*{margin:0;padding:0;box-sizing:border-box}
html,body{width:1200px;height:936px;overflow:hidden;background:var(--bg)}
body{position:relative;font-family:"Arimo",Arial,sans-serif;color:var(--ink)}
.piece{position:absolute;background:var(--paper);box-shadow:0 3px 10px rgba(0,0,0,.22);overflow:hidden}
.piece svg.shape{position:absolute;left:0;top:0;width:100%;height:100%}
.brand{position:absolute;display:flex;align-items:center;gap:6px;font-family:"Michroma",sans-serif;color:var(--band);letter-spacing:.04em;white-space:nowrap}
.brand .mark{display:block;background:var(--accent)}
.small{position:absolute;font-size:6px;line-height:9px;color:var(--muted);white-space:nowrap}
.small .dot{display:inline-block;width:4px;height:4px;border-radius:50%;background:var(--accent);margin-right:4px;vertical-align:middle}

.letterhead{left:172px;top:38px;width:406px;height:579px}
.letterhead .brand{left:26px;top:32px;font-size:13px}
.letterhead .brand .mark{width:12px;height:12px}
.letterhead .watermark{position:absolute;left:0;right:0;top:262px;text-align:center;font-family:"Michroma",sans-serif;font-size:34px;color:var(--faint);letter-spacing:.04em}
.letterhead .contact{left:26px;top:490px}

.folder{left:634px;top:38px;width:520px;height:591px}
.folder .brand{left:0;right:0;top:336px;justify-content:center;font-size:34px;gap:14px}
.folder .brand .mark{width:30px;height:30px}

.card-front{left:38px;top:655px;width:203px;height:101px}
.card-front .brand{left:10px;top:12px;font-size:9px;gap:4px}
.card-front .brand .mark{width:8px;height:8px}
.card-front .contact{left:10px;top:44px;font-size:4.5px;line-height:7px}
.card-front .person{position:absolute;right:10px;top:62px;text-align:right}
.card-front .person .name{font-size:6px;font-weight:700;color:var(--ink)}
.card-front .person .role{font-size:5px;color:var(--accent)}

.card-back{left:38px;top:774px;width:203px;height:101px;background:var(--band)}
.card-back .brand{left:0;right:0;top:38px;justify-content:center;font-size:11px;color:#fff;gap:5px}
.card-back .brand .mark{width:9px;height:9px}
.card-back .web{position:absolute;left:0;right:0;top:70px;text-align:center;font-size:5px;color:var(--accent);letter-spacing:.08em}

.envelope-front{left:266px;top:667px;width:444px;height:208px}
.envelope-front .brand{left:20px;top:16px;font-size:9px;gap:4px}
.envelope-front .brand .mark{width:8px;height:8px}
.envelope-front .contact{left:20px;top:34px;font-size:5px;line-height:7px}

.envelope-back{left:743px;top:667px;width:419px;height:208px}
.envelope-back .web{position:absolute;left:0;right:0;top:34px;text-align:center;font-size:10px;color:#fff;letter-spacing:.14em}
</style>
</head>
<body>

<section class="piece letterhead">
  <svg class="shape" viewBox="0 0 406 579" preserveAspectRatio="none" aria-hidden="true">
    <path d="M150,0 H406 V118 C330,58 240,20 150,0 Z" fill="var(--band)"/>
    <path d="M80,6 C220,26 340,66 406,132" fill="none" stroke="var(--accent)" stroke-width="3"/>
  </svg>
  <div class="brand"><span class="mark"></span>TANDRAFIX</div>
  <div class="watermark">TANDRAFIX</div>
  <div class="small contact">
    <div><span class="dot"></span>40627 NE 73rd Avenue Suite 815</div>
    <div><span class="dot"></span>Harlow Bay, WA 98731</div>
    <div><span class="dot"></span>(360) 555-0148</div>
    <div><span class="dot"></span>dorianw@tandrafix.com</div>
    <div><span class="dot"></span>www.tandrafix.com</div>
  </div>
</section>

<section class="piece folder">
  <svg class="shape" viewBox="0 0 520 591" preserveAspectRatio="none" aria-hidden="true">
    <path d="M170,0 H520 V150 C420,70 300,24 170,0 Z" fill="var(--band)"/>
    <path d="M90,8 C270,36 430,90 520,168" fill="none" stroke="var(--accent)" stroke-width="3.5"/>
  </svg>
  <div class="brand"><span class="mark"></span>TANDRAFIX</div>
</section>

<section class="piece card-front">
  <svg class="shape" viewBox="0 0 203 101" preserveAspectRatio="none" aria-hidden="true">
    <path d="M90,0 H203 V45 C170,24 130,8 90,0 Z" fill="var(--band)"/>
    <path d="M55,3 C125,12 172,30 203,55" fill="none" stroke="var(--accent)" stroke-width="1.5"/>
  </svg>
  <div class="brand"><span class="mark"></span>TANDRAFIX</div>
  <div class="small contact">
    <div>40627 NE 73rd Avenue Suite 815</div>
    <div>Harlow Bay, WA 98731</div>
    <div>(360) 555-0148</div>
    <div>dorianw@tandrafix.com</div>
  </div>
  <div class="person">
    <div class="name">Dorian Welby</div>
    <div class="role">Vice President</div>
  </div>
</section>

<section class="piece card-back">
  <svg class="shape" viewBox="0 0 203 101" preserveAspectRatio="none" aria-hidden="true">
    <path d="M0,8 C80,14 160,40 203,80" fill="none" stroke="var(--accent)" stroke-width="1.5"/>
  </svg>
  <div class="brand"><span class="mark"></span>TANDRAFIX</div>
  <div class="web">www.tandrafix.com</div>
</section>

<section class="piece envelope-front">
  <svg class="shape" viewBox="0 0 444 208" preserveAspectRatio="none" aria-hidden="true">
    <path d="M240,0 H444 V100 C380,48 310,16 240,0 Z" fill="var(--band)"/>
    <path d="M170,4 C290,20 390,58 444,110" fill="none" stroke="var(--accent)" stroke-width="2"/>
  </svg>
  <div class="brand"><span class="mark"></span>TANDRAFIX</div>
  <div class="small contact">
    <div>40627 NE 73rd Avenue Suite 815, Harlow Bay, WA 98731</div>
  </div>
</section>

<section class="piece envelope-back">
  <svg class="shape" viewBox="0 0 419 208" preserveAspectRatio="none" aria-hidden="true">
    <rect width="419" height="208" fill="var(--band)"/>
    <path d="M0,208 V120 C140,150 300,150 419,105 V208 Z" fill="var(--paper)"/>
    <path d="M0,116 C140,146 300,146 419,101" fill="none" stroke="var(--accent)" stroke-width="2"/>
  </svg>
  <div class="web">www.tandrafix.com</div>
</section>

</body>
</html>
```